Business Card Design Project

I am a Chiropractor that is looking for a new business card.  Our logo was slightly changed lately, therefore need a new, more professional look.
We are a modern, non-stuffy chiropractic office.  Want a contemporary look that will let people know this is not your typical doctors office.  Our logo is red, and contains the name of our business: realign.  The u in the logo is green, stressing the most important part of our business: "u"

Target Market(s)
moderate to upper income bracket, family friendly
www.realignspine-example.com
Gordon Pell
Family Chiropractor
314 Hollis Rd
Bastrop, TX 78999
512.555.0147 phone
512.555.0148 fax
Industry/Entity Type
Business
Requirements
Must have
- www.realignspine-example.com
Gordon Pell
Family Chiropractor
314 Hollis Rd
Bastrop, TX 78999
512.555.0147 phone
512.555.0148 fax

```html
<!DOCTYPE html>
<html lang="en">
<head>
<meta charset="utf-8">
<title>realign – business card</title>
<link href="https://fonts.googleapis.com/css2?family=Arimo:wght@400;700&display=swap" rel="stylesheet">
<style>
  :root {
    --page: #ffffff;
    --green: #6db33f;
    --green-top: #7ab648;
    --green-pale: #dde9cf;
    --red: #ec3b31;
    --red-dark: #c0443c;
    --red-soft: #f4a7a1;
    --ink: #555555;
    --white: #ffffff;
  }
  * { margin: 0; padding: 0; box-sizing: border-box; }
  html, body {
    width: 1200px; height: 901px; overflow: hidden;
    background: var(--page);
    font-family: "Arimo", Arial, sans-serif;
  }
  .canvas { position: relative; width: 1200px; height: 901px; }
  .card {
    position: absolute; left: 295px; width: 612px; height: 350px;
    overflow: hidden;
    box-shadow: 3px 4px 6px rgba(0,0,0,0.28);
  }
  .card--front { top: 52px; }
  .card--back { top: 485px; }
  .card__art { position: absolute; inset: 0; width: 612px; height: 350px; display: block; }
  .brand-name {
    position: absolute; color: var(--red); font-weight: 400;
    letter-spacing: 1px; line-height: 1; white-space: nowrap;
  }
  .card--front .brand-name { left: 0; width: 612px; text-align: center; top: 128px; font-size: 66px; }
  .card--back .brand-name { left: 64px; top: 84px; font-size: 52px; }
  .web {
    position: absolute; color: var(--white); font-size: 17px; line-height: 1;
  }
  .card--front .web { left: 0; width: 612px; text-align: center; top: 314px; }
  .card--back .web { left: 68px; top: 313px; }
  .contact { position: absolute; left: 391px; top: 119px; color: var(--ink); font-size: 16px; line-height: 21px; }
  .contact__name { color: var(--green); font-weight: 700; font-size: 19px; line-height: 22px; }
  .contact__title { margin-bottom: 21px; }
  .contact__line { display: flex; align-items: center; gap: 6px; }
  .contact__icon { width: 15px; height: 13px; flex: none; }
</style>
</head>
<body>
<div class="canvas">

  <section class="card card--front">
    <svg class="card__art" viewBox="0 0 612 350" aria-hidden="true">
      <defs>
        <linearGradient id="frontSky" x1="0" y1="0" x2="0" y2="1">
          <stop offset="0" stop-color="#7ab648"/>
          <stop offset="1" stop-color="#e4eed8"/>
        </linearGradient>
        <linearGradient id="swoosh" x1="0" y1="0" x2="1" y2="0">
          <stop offset="0" stop-color="#c0443c"/>
          <stop offset="0.5" stop-color="#ec3b31"/>
          <stop offset="1" stop-color="#f4a7a1"/>
        </linearGradient>
      </defs>
      <rect width="612" height="350" fill="url(#frontSky)"/>
      <path d="M0,218 Q320,330 612,268 L612,350 L0,350 Z" fill="url(#swoosh)"/>
      <path d="M0,245 Q320,320 612,303 L612,350 L0,350 Z" fill="var(--green)"/>
    </svg>
    <div class="brand-name">realign</div>
    <div class="web">www.realignspine-example.com</div>
  </section>

  <section class="card card--back">
    <svg class="card__art" viewBox="0 0 612 350" aria-hidden="true">
      <defs>
        <linearGradient id="backSky" x1="0" y1="0" x2="0" y2="1">
          <stop offset="0" stop-color="#c4dcae"/>
          <stop offset="0.34" stop-color="#ffffff"/>
          <stop offset="1" stop-color="#ffffff"/>
        </linearGradient>
        <linearGradient id="swooshBack" x1="0" y1="0" x2="1" y2="0">
          <stop offset="0" stop-color="#c0443c"/>
          <stop offset="0.5" stop-color="#ec3b31"/>
          <stop offset="1" stop-color="#f4a7a1"/>
        </linearGradient>
      </defs>
      <rect width="612" height="350" fill="url(#backSky)"/>
      <path d="M0,228 Q320,345 612,276 L612,350 L0,350 Z" fill="url(#swooshBack)"/>
      <path d="M0,256 Q320,336 612,311 L612,350 L0,350 Z" fill="var(--green)"/>
    </svg>
    <div class="brand-name">realign</div>
    <div class="contact">
      <div class="contact__name">Gordon Pell</div>
      <div class="contact__title">Family Chiropractor</div>
      <div>314 Hollis Rd</div>
      <div>Bastrop, TX 78999</div>
      <div class="contact__line">
        <svg class="contact__icon" viewBox="0 0 15 13" role="img" aria-label="phone">
          <path d="M1,4 Q7.5,-1 14,4 L12,6 L10,5 L10,4 Q7.5,3 5,4 L5,5 L3,6 Z" fill="var(--red)"/>
          <path d="M3,7 L5,5.5 L10,5.5 L12,7 L12,12 L3,12 Z" fill="var(--red)"/>
          <circle cx="7.5" cy="9" r="1.6" fill="var(--white)"/>
        </svg>
        <span>512.555.0147</span>
      </div>
      <div class="contact__line">
        <svg class="contact__icon" viewBox="0 0 15 13" role="img" aria-label="fax">
          <rect x="4" y="0.5" width="7" height="4" fill="var(--red)"/>
          <rect x="1" y="4" width="13" height="6" rx="1" fill="var(--red)"/>
          <rect x="4" y="8" width="7" height="4.5" fill="var(--white)" stroke="var(--red)" stroke-width="1"/>
        </svg>
        <span>512.555.0148</span>
      </div>
    </div>
    <div class="web">www.realignspine-example.com</div>
  </section>

</div>
</body>
</html>
```